Real Estate agent needs flyer/folder to contain bio and overview of services

I'm including files of the layout of the small folder. The folder is 6 1/2 across and 9 1/2 inches long. It will have a front & back cover and then writing on the 2 inside pages.

I am sending a few files to incorporate into the flyer, 1 new logo to use and 2 files which are coloring ideas.

Colors

Designer to choose colors to be used in the design.

```html
<!DOCTYPE html>
<html lang="en">
<head>
<meta charset="utf-8">
<title>Real Estate Folder – Inside Spread</title>
<link href="https://fonts.googleapis.com/css2?family=Arimo:wght@400;700&display=swap" rel="stylesheet">
<style>
  :root {
    --backdrop: #e4e4e4;
    --page-left: #ffffff;
    --page-right: #ededed;
    --teal: #2e8e96;
    --ink: #6b6b6b;
    --photo-sky: #b9c6dc;
    --photo-house: #5c6d8c;
    --photo-grass: #7fbf4a;
    --photo-villa: #efe6da;
    --photo-roof: #b7805c;
    --photo-blue: #6e8fb8;
    --photo-desk: #d9dde0;
  }
  * { box-sizing: border-box; margin: 0; padding: 0; }
  html, body { width: 1200px; height: 897px; overflow: hidden; }
  body {
    background: var(--backdrop);
    font-family: "Arimo", Arial, sans-serif;
    color: var(--ink);
    position: relative;
  }
  .spread {
    position: absolute; left: 30px; top: 31px;
    width: 1140px; height: 834px;
    display: flex;
    box-shadow: 0 6px 22px rgba(0,0,0,.18);
  }
  .page { position: relative; width: 570px; height: 834px; overflow: hidden; }
  .page--left { background: var(--page-left); }
  .page--right { background: var(--page-right); }

  .section-title {
    color: var(--teal); font-weight: 700; font-size: 15px;
    text-transform: uppercase; letter-spacing: -.2px; margin-bottom: 5px;
  }
  .body-copy { font-size: 11.2px; line-height: 1.32; }
  .section { margin-bottom: 14px; }

  /* left page */
  .photo { position: absolute; }
  .photo--house-dusk { left: 22px; top: 40px; width: 150px; height: 136px;
    background: linear-gradient(180deg, var(--photo-sky) 0%, #8d9cbc 45%, var(--photo-house) 75%, #9aa4b1 100%); }
  .photo--city-lawn { left: 22px; top: 186px; width: 180px; height: 156px;
    background: radial-gradient(ellipse at 60% 80%, var(--photo-grass) 0%, #a7cf85 30%, #eef0f2 62%, #f3f4f5 100%); }
  .photo--villa-a { left: 22px; top: 350px; width: 200px; height: 140px;
    background: linear-gradient(180deg, #8fbde6 0%, #cfe1f1 30%, var(--photo-villa) 50%, var(--photo-roof) 58%, var(--photo-villa) 66%, #c9c3b5 85%, #8fa86a 100%); }
  .photo--villa-b { left: 22px; top: 498px; width: 200px; height: 140px;
    background: linear-gradient(180deg, #8fbde6 0%, #cfe1f1 30%, var(--photo-villa) 50%, var(--photo-roof) 58%, var(--photo-villa) 66%, #c9c3b5 85%, #8fa86a 100%); }
  .photo--blue-model { left: 22px; top: 660px; width: 190px; height: 150px;
    background: radial-gradient(ellipse at 50% 45%, var(--photo-blue) 0%, #8fa7c6 38%, #e9ecef 70%, #f7f7f7 100%); }

  .left-copy { position: absolute; top: 36px; }
  .left-copy--intro { left: 190px; width: 356px; }
  .left-copy--lower { left: 232px; top: 262px; width: 316px; }
  .left-copy--selling { left: 222px; top: 668px; width: 326px; }

  /* right page */
  .right-copy { position: absolute; left: 40px; top: 40px; width: 492px; }
  .right-copy .section { margin-bottom: 22px; }
  .photo-band {
    position: absolute; left: 0; bottom: 0; width: 570px; height: 276px;
    border-top: 5px solid var(--teal);
  }
  .photo-band__desk { position: absolute; inset: 0;
    background: linear-gradient(160deg, #f1f2f3 0%, var(--photo-desk) 45%, #c4cace 100%); }
  .photo-band__city { position: absolute; right: 0; top: 0; width: 250px; height: 100%;
    background: radial-gradient(ellipse at 55% 70%, var(--photo-grass) 0%, #9ccc77 35%, rgba(226,230,233,.4) 70%, rgba(226,230,233,0) 100%); }
</style>
</head>
<body>
<main class="spread">
  <section class="page page--left">
    <div class="photo photo--house-dusk" role="img" aria-label="Photo of a two-storey family home at dusk with lit windows"></div>
    <div class="photo photo--city-lawn" role="img" aria-label="Illustration of a modern house on a green lawn in front of city towers"></div>
    <div class="photo photo--villa-a" role="img" aria-label="Photo of a white Mediterranean villa with tiled roof"></div>
    <div class="photo photo--villa-b" role="img" aria-label="Photo of a white Mediterranean villa with tiled roof"></div>
    <div class="photo photo--blue-model" role="img" aria-label="Blue house model resting on architectural plans"></div>

    <div class="left-copy left-copy--intro">
      <h2 class="section-title">Let Me Introduce Myself:</h2>
      <p class="body-copy">I'm originally from Chicago, but I'm a full-fledged California girl now. I've lived and worked in Orange County since 1996. I always say where we live is the next best thing to living on a tropical island. I've traveled to many and I'm always happy to come back to my Laguna Niguel home. My passion for this area is why I'm in Real Estate. I consider myself incredibly fortunate to sell homes and help people purchase homes in an area that I love with all my heart. This passion also carries over in representing my clients with the highest degree of professionalism, enthusiasm and care. My business is built on exceptional customer service and I'm grateful my clients are mostly repeat and referrals.</p>
    </div>

    <div class="left-copy left-copy--lower">
      <div class="section">
        <h2 class="section-title">My Core Tenet:</h2>
        <p class="body-copy">It's All About YOU!<br>My 1 priority is understanding your needs and your objectives.<br>This understanding, along with working diligently on your behalf, means we accomplish your goal whether you're purchasing your 1st home or selling a home you've loved so you can move on to the next chapter of your life.</p>
      </div>
      <div class="section">
        <h2 class="section-title">Real Estate Services &amp; Beyond:</h2>
        <p class="body-copy">Simply put, I help people who are local, relocating and investing, sell and purchase homes in Southern California. For purchases outside of California, I can refer to a network of agents across the country. I also provide a team who is dedicated to providing outstanding customer service throughout the transaction. My team includes a network of lenders, title, and escrow officers, in house CPA, stagers, photographers, contractors and more.</p>
      </div>
    </div>

    <div class="left-copy left-copy--selling">
      <h2 class="section-title">Selling Your Home</h2>
      <p class="body-copy">Selling your home is not like any other business transaction. It's also personal. My priority as your Listing Agent is to guide you through what can be a complicated and sometimes emotional process. I place great emphasis on marketing your property with professional photographs, along with harnessing the Power.</p>
    </div>
  </section>

  <section class="page page--right">
    <div class="right-copy">
      <div class="section">
        <h2 class="section-title">Buying a Home</h2>
        <p class="body-copy">If you're thinking about buying a home, it's imperative you have an accomplished, real estate professional by your side to walk you through what is likely the largest purchase of your life. To get started, I like to meet with you so we have an opportunity to get to know each other as purchasing a home is a uniquely personal endeavor. At that time, we can discuss your goals and if it's a good time for you to purchase a home. From there, the first step is to obtain a pre-approval from a lender. I'm able to recommend various lenders who can introduce and explain the various loan products available. After you've been pre-approved, that's when the fun starts! I guide you through the home buying adventure every step of the way and look forward to handing you the keys to your new home.</p>
      </div>
      <div class="section">
        <h2 class="section-title">Testimonials:</h2>
        <p class="body-copy">Dana got us an amazing deal on our new home and sold our old home in a week. Dana is patient, hardworking, professional and most importantly HONEST. Dana is definitely one of the best in the business! Maya &amp; Owen Reyes<br>Dana is the kind of Real Estate professional everyone wants to represent them. She is knowledgeable, ethical, energetic, and follows up on every detail. Her honesty, integrity and expertise combined make her a very special and remarkable professional. We were lucky to find her! Grant &amp; Lena Hollis<br>During the home buying process, Dana becomes your trusted advisor, mentor and friend. Her knowledge of the industry, community and market are best in class. A true professional! Dana aligned her goals with my own and understood the motivation behind my purchase. Dana is unequivocally the reason why I was able to purchase my home in Laguna Niguel and provide my family with a world-class community. Without her guidance and experience I would still be in the market attempting to navigate the ever-changing work of real estate. Tomas Averill</p>
      </div>
    </div>
    <div class="photo-band">
      <div class="photo-band__desk" role="img" aria-label="Photo of a pen resting on printed charts on a desk"></div>
      <div class="photo-band__city" role="img" aria-label="Illustration of modern homes on a green lawn before city towers"></div>
    </div>
  </section>
</main>
</body>
</html>
```